New Website for Belcourt Manor at www.belcourt.com.au

A new logo has been designed (through pixel forge) and we now want to align the look and feel of our website at www.belcourt.com.au to the new logo. The content and page names (e.g. Grounds) will remain largely unchanged for the new site, so please submit a new look "Home" page, using our new logo, current text and any photos you choose from the existing gallery at our website. I have also attached the current "Home" page photos.

Industry/Entity Type

Accommodation

Number of Pages Required

1 page

Requirements
Must have
• Logo to be presented on white background.

```html
<!DOCTYPE html>
<html lang="en">
<head>
<meta charset="utf-8">
<title>Belcourt Manor – Home</title>
<link href="https://fonts.googleapis.com/css2?family=Roboto:wght@400;500;700;900&display=swap" rel="stylesheet">
<style>
:root{
  --blue:#1a6db5;
  --blue-dark:#0f5fa8;
  --ink:#2c2c2c;
  --gold:#f3c21c;
  --band:#f4f5f7;
  --white:#ffffff;
}
*{margin:0;padding:0;box-sizing:border-box}
html,body{width:1200px;height:3562px;overflow:hidden;background:var(--white)}
body{position:relative;font-family:'Roboto',sans-serif;color:var(--ink)}
.abs{position:absolute}
.site-header{left:0;top:0;width:1200px;height:88px;background:var(--band)}
.brand{left:65px;top:24px;display:flex;align-items:center;gap:10px;font-size:24px;font-weight:500;color:var(--blue)}
.brand-dot{width:18px;height:18px;border-radius:50%;background:var(--gold)}
.main-nav{right:61px;top:36px;font-size:11px;font-weight:700;letter-spacing:1.3px;color:var(--blue);white-space:nowrap}
.main-nav span{color:var(--ink);font-weight:400;margin:0 4px}
.hero{left:0;top:88px;width:1200px;height:609px;background:linear-gradient(180deg,#6f8a4a 0%,#c97a4a 25%,#d9b86a 45%,#4e8a52 65%,#37a7b8 85%,#3d6d3a 100%)}
.hero-title{left:0;top:340px;width:1200px;text-align:center;font-size:56px;font-weight:900;letter-spacing:8px;color:var(--white)}
.hero-sub{left:0;top:408px;width:1200px;text-align:center;font-size:22px;font-weight:700;letter-spacing:7px;color:var(--gold)}
.section-title{font-size:20px;font-weight:700;letter-spacing:3px;color:var(--blue);text-align:center}
.copy{font-size:12px;line-height:22.5px;letter-spacing:1.2px;color:var(--ink)}
.copy a{color:var(--blue);font-weight:700;text-decoration:none}
.btn{display:flex;align-items:center;justify-content:center;background:var(--blue-dark);color:var(--white);font-size:11px;font-weight:700;letter-spacing:1.5px;border-radius:2px}
.about{left:0;top:697px;width:1200px;height:463px;background:var(--band)}
.about-photo{left:608px;top:697px;width:592px;height:463px;background:linear-gradient(90deg,var(--band) 0%,#b9c9a8 18%,#d9764a 45%,#e3c46a 70%,#5a7f4a 100%)}
.mansion-photo{left:0;top:1160px;width:594px;height:524px;background:linear-gradient(90deg,#6b6a5e 0%,#d8d4cc 40%,#ece9e4 75%,var(--white) 100%)}
.bedrooms{left:0;top:1684px;width:1200px;height:452px;background:var(--band)}
.room-photo{top:1796px;width:347px;height:228px}
.map{left:0;top:2136px;width:1200px;height:740px;background:linear-gradient(135deg,#4a5a48 0%,#6a6e60 45%,#5a6258 70%,#3f4d45 100%)}
.map-title{left:0;top:2240px;width:1200px;text-align:center;font-size:28px;font-weight:500;letter-spacing:5px;color:var(--white)}
.weddings{left:0;top:2876px;width:1200px;height:493px;background:var(--band)}
.wedding-photo{top:3169px;width:138px;height:138px;border-radius:50%}
.badge{top:3155px;width:30px;height:30px;border-radius:50%;background:var(--blue-dark);display:flex;align-items:center;justify-content:center}
.footer-links,.footer-copy{top:3457px;font-size:13px;font-weight:500;letter-spacing:2px;color:var(--ink)}
.footer-links span{color:var(--blue);margin:0 6px}
</style>
</head>
<body>

<header class="abs site-header"></header>
<div class="abs brand"><div class="brand-dot"></div>Belcourt Manor</div>
<nav class="abs main-nav">MAIN<span>|</span>MANSION<span>|</span>BEDROOMS<span>|</span>OPTIONS<span>|</span>FOX AND HOUND<span>|</span>GROUNDS<span>|</span>LOCATION<span>|</span>GALLERY<span>|</span>CONTACT<span>|</span>AVAILABILITY<span>|</span>DIY WEDDINGS</nav>

<section class="abs hero" role="img" aria-label="Aerial photo of the manor with terracotta roofs, tropical garden and pool"></section>
<h1 class="abs hero-title">BELCOURT MANOR</h1>
<p class="abs hero-sub">PALATIAL ESTATE AND LUXURY RESORT</p>

<section class="abs about"></section>
<div class="abs about-photo" role="img" aria-label="Photo of the yellow manor house with red tile roof among trees"></div>
<h2 class="abs section-title" style="left:200px;top:748px;width:202px">ABOUT US</h2>
<p class="abs copy" style="left:120px;top:813px;width:370px">On over 2 manicured garden acres, Belcourt Manor is a unique Sunshine Bay estate, centrally located in the prestigious rural suburb of Glenview.&nbsp; <a>More about our Location</a></p>
<p class="abs copy" style="left:120px;top:926px;width:370px">The estate features a grand mansion, private pub (The Fox and Hound), sparkling resort pool, tennis court and playground...</p>
<div class="abs btn" style="left:228px;top:1073px;width:138px;height:35px">LEARN MORE</div>

<div class="abs mansion-photo" role="img" aria-label="Photo of the mansion interior with columns, balcony railing and lounge"></div>
<h2 class="abs section-title" style="left:780px;top:1267px;width:300px">GRAND MANSION</h2>
<p class="abs copy" style="left:722px;top:1374px;width:390px">Lorem ipsum dolor sit amet, consectetur adipiscing elit, sed do eiusmod tempor incididunt ut labore et dolore magna aliqua. Ut enim ad minim veniam, quis nostrud exercitation ullamco laboris nisi ut aliquip ex ea commodo consequat.</p>
<div class="abs btn" style="left:861px;top:1576px;width:138px;height:35px">LEARN MORE</div>

<section class="abs bedrooms"></section>
<h2 class="abs section-title" style="left:107px;top:1764px;width:200px">BEDROOMS</h2>
<p class="abs copy" style="left:117px;top:1832px;width:180px;text-align:center">All Suites feature ensuites, walk-in robes, TVs and DVD players – and the kids will tell you the Bunk Room is "like cool and awesome"!</p>
<div class="abs btn" style="left:152px;top:2022px;width:109px;height:28px;font-size:9px">LEARN MORE</div>
<svg class="abs" style="left:1040px;top:1760px" width="42" height="18" viewBox="0 0 42 18" aria-label="Previous and next">
  <path d="M9 3 L3 9 L9 15" fill="none" stroke="#1a6db5" stroke-width="2.4"/>
  <path d="M31 3 L37 9 L31 15" fill="none" stroke="#1a6db5" stroke-width="2.4"/>
</svg>
<div class="abs room-photo" style="left:362px;background:linear-gradient(180deg,#d8d2c8 0%,#8c9a7a 45%,#3f5f55 100%)" role="img" aria-label="Photo of a bedroom with garden view doors and TV"></div>
<div class="abs room-photo" style="left:731px;background:linear-gradient(180deg,#ddd6c8 0%,#9a6a48 50%,#3a4a8a 100%)" role="img" aria-label="Photo of a bedroom with timber beds and blue quilts"></div>

<section class="abs map" role="img" aria-label="Satellite map of the area showing the estate and nearby shops, stadium, hospital and station"></section>
<h2 class="abs map-title">OUR LOCATION - 27 BELCOURT DRIVE, GLENVIEW</h2>

<section class="abs weddings"></section>
<h2 class="abs section-title" style="left:400px;top:2923px;width:400px">DIY WEDDINGS</h2>
<p class="abs copy" style="left:0;top:3001px;width:1200px;text-align:center;font-weight:700;font-size:11px">Do It Yourself Weddings at Belcourt Manor</p>
<p class="abs copy" style="left:200px;top:3047px;width:800px;text-align:center;font-size:11px">Properties such as Belcourt Manor are accommodation houses for short-term holidays – they are not licensed to operate as Reception or Function Centres.</p>

<div class="abs wedding-photo" style="left:288px;background:linear-gradient(180deg,#c96a4a,#3a3a4a)" role="img" aria-label="Photo of wedding guests outside the house"></div>
<div class="abs wedding-photo" style="left:456px;background:linear-gradient(180deg,#3a4a6a,#e8e8ee)" role="img" aria-label="Photo of a wedding table set outdoors"></div>
<div class="abs wedding-photo" style="left:626px;background:linear-gradient(180deg,#e0b870,#7a3a2a)" role="img" aria-label="Photo of a dinner reception indoors"></div>
<div class="abs wedding-photo" style="left:796px;background:linear-gradient(180deg,#dfe6ea,#5a7a5a)" role="img" aria-label="Photo of a couple in a garden gazebo"></div>

<div class="abs badge" style="left:342px"><svg width="16" height="12" viewBox="0 0 16 12"><rect x="1" y="3" width="14" height="8" rx="1.5" fill="#f3c21c"/><rect x="5" y="1" width="6" height="3" fill="#f3c21c"/><circle cx="8" cy="7" r="2.4" fill="#0f5fa8"/></svg></div>
<div class="abs badge" style="left:510px"><svg width="16" height="12" viewBox="0 0 16 12"><rect x="1" y="3" width="14" height="8" rx="1.5" fill="#f3c21c"/><rect x="5" y="1" width="6" height="3" fill="#f3c21c"/><circle cx="8" cy="7" r="2.4" fill="#0f5fa8"/></svg></div>
<div class="abs badge" style="left:680px"><svg width="16" height="12" viewBox="0 0 16 12"><rect x="1" y="3" width="14" height="8" rx="1.5" fill="#f3c21c"/><rect x="5" y="1" width="6" height="3" fill="#f3c21c"/><circle cx="8" cy="7" r="2.4" fill="#0f5fa8"/></svg></div>
<div class="abs badge" style="left:850px"><svg width="16" height="12" viewBox="0 0 16 12"><rect x="1" y="3" width="14" height="8" rx="1.5" fill="#f3c21c"/><rect x="5" y="1" width="6" height="3" fill="#f3c21c"/><circle cx="8" cy="7" r="2.4" fill="#0f5fa8"/></svg></div>

<footer>
  <div class="abs footer-links" style="left:54px">CREDITS<span>|</span>PRIVACY<span>|</span>OUR TEAMS</div>
  <div class="abs footer-copy" style="right:61px">COPYRIGHT BY BELCOURT - ALL RIGHT RESERVED</div>
</footer>

</body>
</html>
```